Baby Store - GIF Banner

About the Company:
Nalifa.com.sa is an online shop for baby related products in Saudi Arabia. The targeted audience is moms between 25-35 years of age. The word "Nalifa" means Shop/Store in the Arabic Language.
About the Banner:
The banners should be designed in animated GIF format and provide in four sizes, upon clicking on the banner it will take you to Nalifa website. The Banners will convey the following:
- All your baby daily needs
مستلزمات طفلك اليومية من نليفا
- Free same day delivery
توصيل مجاني بنفس اليوم في الرياض
- Subscribe now for special discounts.
سجلي الان لتحصلي على خصم خاص
Note: Arabic Text are attached in PSD format.
Design Requirements:
Company Logo is attached.
Sample of product photos will be provided.
Baby photo can be used.
Shop Now Button should be included in the design.
تسوق الان
Shop Now
Logo colors are the main colors to be used (Blue, Pink, Gray)
DropBox Link: will be provided upon request.
Design Style:
- Play full
- Feminine
- Creative
Delivery Requirements:
Initially we may start working on an English version, at the end you will must to provide an Arabic version of the Banners in addition to the English version. Arabic translations are provided above, Note that Arabic language is from right to left opposite to the English language.
Banners Sizes Required:
Banner 1: 728 x 90
Banner 2: 480 x 70
Banner 3: 300 x 250
Banner 4: 648x40
Banner Specs:
Size less than 100 kb
Background less than 80% alpha
Please pay EXTRA attention to the guidelines in the following link:
https://help.brivantomedia.net/clips/answer/530418
If you have any questions please let me know, wish you the best of luck.
Modern Moms of age 25-35.
Shop

```html
<!DOCTYPE html>
<html lang="ar">
<head>
<meta charset="utf-8">
<title>Nalifa.com.sa – Banners</title>
<link rel="stylesheet" href="https://fonts.googleapis.com/css2?family=Noto+Sans+Arabic:wght@400;500;600&display=swap">
<style>
  :root {
    --board: #3a3839;
    --pink: #ec5d9f;
    --pink-stripe: #f06aa8;
    --pink-line: rgba(255,255,255,0.06);
    --blue: #4aa8e8;
    --blue-light: #7ec4f1;
    --gray: #555556;
    --white: #ffffff;
    --edge: #c9c9c9;
  }
  html, body {
    margin: 0;
    width: 1200px;
    height: 900px;
    overflow: hidden;
    background: var(--board);
    font-family: "Noto Sans Arabic", sans-serif;
  }
  .board { position: relative; width: 1200px; height: 900px; }
  .banner {
    position: absolute;
    left: 163px;
    width: 874px;
    height: 108px;
    background-color: var(--pink);
    background-image:
      repeating-linear-gradient(135deg, var(--pink-line) 0 1px, transparent 1px 4px),
      repeating-linear-gradient(90deg, var(--pink) 0 7px, var(--pink-stripe) 7px 14px);
    outline: 1px solid var(--edge);
    overflow: hidden;
  }
  .banner-1 { top: 127px; }
  .banner-2 { top: 283px; }
  .banner-3 { top: 440px; }
  .banner-4 { top: 596px; }
  .brand-panel { position: absolute; left: 0; top: 0; width: 220px; height: 108px; }
  .brand {
    position: absolute;
    left: 17px;
    top: 14px;
    direction: ltr;
  }
  .brand-name {
    display: flex;
    align-items: center;
    gap: 6px;
    font-size: 38px;
    font-weight: 600;
    line-height: 48px;
    color: var(--blue);
  }
  .brand-dot {
    width: 12px; height: 12px;
    border-radius: 50%;
    background: var(--pink);
  }
  .brand-domain {
    font-size: 19px;
    line-height: 22px;
    color: var(--gray);
    letter-spacing: 0.5px;
  }
  .message {
    position: absolute;
    top: 0;
    margin: 0;
    height: 108px;
    line-height: 1;
    display: flex;
    align-items: center;
    direction: rtl;
    color: var(--white);
    font-size: 31px;
    font-weight: 400;
    white-space: nowrap;
  }
  .banner-1 .message, .banner-2 .message, .banner-3 .message { right: 197px; }
  .banner-4 .message { right: 56px; }
  .visual { position: absolute; top: 0; height: 108px; }
  .visual-baby { left: 713px; width: 161px; background: linear-gradient(160deg, #f6dccb, #e9bca3 60%, #f3e6e8); }
  .visual-bottle { left: 723px; width: 74px; background: linear-gradient(180deg, #e8c23a, #d9a514 60%, #c98e0c); }
  .visual-pacifier { left: 697px; width: 177px; background: radial-gradient(ellipse at 55% 45%, #c9ecf7, #7fcde9 55%, rgba(236,93,159,0) 80%); }
  .cta {
    position: absolute;
    left: 238px;
    top: 23px;
    width: 227px;
    height: 61px;
    box-sizing: border-box;
    border: 2px solid var(--blue-light);
    border-radius: 4px;
    background: var(--blue);
    color: var(--white);
    font-size: 28px;
    line-height: 1;
    text-decoration: none;
    display: flex;
    align-items: center;
    justify-content: center;
    direction: rtl;
  }
</style>
</head>
<body>
<main class="board">

  <section class="banner banner-1">
    <svg class="brand-panel" viewBox="0 0 220 108" aria-hidden="true">
      <polygon points="0,0 203,0 190,108 0,108" fill="var(--white)"/>
      <polygon points="203,0 212,0 199,108 190,108" fill="var(--blue)"/>
    </svg>
    <div class="brand">
      <div class="brand-name">Nalifa<span class="brand-dot"></span></div>
      <div class="brand-domain">.COM.SA</div>
    </div>
    <p class="message">مستلزمات طفلك اليومية من نليفا</p>
    <div class="visual visual-baby" role="img" aria-label="Photo of a smiling baby holding a toy"></div>
  </section>

  <section class="banner banner-2">
    <svg class="brand-panel" viewBox="0 0 220 108" aria-hidden="true">
      <polygon points="0,0 203,0 190,108 0,108" fill="var(--white)"/>
      <polygon points="203,0 212,0 199,108 190,108" fill="var(--blue)"/>
    </svg>
    <div class="brand">
      <div class="brand-name">Nalifa<span class="brand-dot"></span></div>
      <div class="brand-domain">.COM.SA</div>
    </div>
    <p class="message">حفاضات، حليب، شامبو وأكثر ...</p>
    <div class="visual visual-bottle" role="img" aria-label="Product photo of a bottle of baby shampoo"></div>
  </section>

  <section class="banner banner-3">
    <svg class="brand-panel" viewBox="0 0 220 108" aria-hidden="true">
      <polygon points="0,0 203,0 190,108 0,108" fill="var(--white)"/>
      <polygon points="203,0 212,0 199,108 190,108" fill="var(--blue)"/>
    </svg>
    <div class="brand">
      <div class="brand-name">Nalifa<span class="brand-dot"></span></div>
      <div class="brand-domain">.COM.SA</div>
    </div>
    <p class="message">توصيل مجاني بنفس اليوم في الرياض</p>
    <div class="visual visual-pacifier" role="img" aria-label="Product photo of a light blue baby pacifier"></div>
  </section>

  <section class="banner banner-4">
    <svg class="brand-panel" viewBox="0 0 220 108" aria-hidden="true">
      <polygon points="0,0 203,0 190,108 0,108" fill="var(--white)"/>
      <polygon points="203,0 212,0 199,108 190,108" fill="var(--blue)"/>
    </svg>
    <div class="brand">
      <div class="brand-name">Nalifa<span class="brand-dot"></span></div>
      <div class="brand-domain">.COM.SA</div>
    </div>
    <a class="cta" href="https://nalifa.com.sa">سجلي الان</a>
    <p class="message">لتحصلي على خصم خاص</p>
  </section>

</main>
</body>
</html>
```